Redwing Hall Sports Bar & Grill Dining Room Menu

Looking for Dining room menus similar to the ones attached from Q8's. I think those are 8.5x14. Would like the main menu to be One page both sides, and then a seperate page that is just for Mosaic Pizza. This is a sports bar and grill. Would like it to be colorful and fun with some food pics, not all text. I have attached a copy of our current carryout menu. All menu items and prices can go into the new design. There will be a few revisions on items once we get the design right. You can use the attached logo but we are looking for a new design
Target Market(s)
Sports Bar
Industry/Entity Type
Sports Bar
Colors
Designer to choose colors to be used in the design.
Requirements
Nice to have
- Pictures, I do have some food pics if we need them

```html
<!DOCTYPE html>
<html lang="en">
<head>
<meta charset="utf-8">
<title>Redwing Hall Sports Bar &amp; Grill – Dining Room Menu</title>
<link href="https://fonts.googleapis.com/css2?family=Montserrat:wght@600;700;800&family=Lora:ital,wght@0,400;0,600;1,400&family=Satisfy&display=swap" rel="stylesheet">
<style>
:root{
  --stage:#3b3e45;
  --paper:#fbfbf9;
  --red:#ad2436;
  --navy:#1f3d70;
  --teal:#2b6c80;
  --tan:#c9a777;
  --blue:#5d8fc4;
  --ink:#3d3d3d;
  --muted:#777;
}
*{box-sizing:border-box;margin:0;padding:0}
html,body{width:1200px;height:800px;overflow:hidden;background:var(--stage)}
.spread{position:absolute;left:30px;top:30px;width:1140px;height:740px;display:flex}
.page{position:relative;width:570px;height:740px;overflow:hidden}
.border-band{position:absolute;inset:0}
.page--left .border-band{background:linear-gradient(135deg,var(--teal) 0%,var(--tan) 50%,var(--teal) 100%)}
.page--right .border-band{background:linear-gradient(135deg,var(--red) 0%,var(--blue) 50%,var(--red) 100%)}
.sheet{position:absolute;inset:22px;background:var(--paper)}
.art{position:absolute;border-radius:8px}
.sec-title{font:800 17px/1 "Montserrat",sans-serif;letter-spacing:3px;color:var(--red);text-transform:uppercase}
.sub-title{font:700 12px/1 "Montserrat",sans-serif;letter-spacing:2px;color:var(--navy);text-transform:uppercase}
.script{font-family:"Satisfy",cursive;font-weight:400;color:var(--red)}
.col{position:absolute}
.item{margin-bottom:8px}
.item h3{font:700 10px/1.2 "Montserrat",sans-serif;color:var(--navy);text-transform:uppercase;letter-spacing:.5px}
.item h3 .price{color:var(--red);margin-left:4px}
.item p{font:400 8.5px/1.3 "Lora",serif;color:var(--ink)}
.note{font:italic 400 8.5px/1.3 "Lora",serif;color:var(--muted)}
.more{font:700 9px/1 "Montserrat",sans-serif;color:var(--red);text-transform:uppercase}
.bev-brand{font:600 20px/1 "Lora",serif;color:var(--red)}
.bev-list{font:700 10px/1.45 "Montserrat",sans-serif;color:var(--navy);text-transform:uppercase}
.bev-list .hl{color:var(--red)}
.dots{border-top:3px dotted var(--navy);width:150px;margin:8px 0}
.kids li{list-style:none;font:700 9.5px/1.5 "Montserrat",sans-serif;color:var(--red);text-transform:uppercase}
</style>
</head>
<body>
<main class="spread">

  <section class="page page--left">
    <div class="border-band" role="img" aria-label="Teal and tan chevron border pattern"></div>
    <div class="sheet"></div>

    <div class="art" style="left:300px;top:36px;width:115px;height:95px;background:radial-gradient(circle at 40% 50%,#8fb36a,#d8cfb8 70%,#f3eee4)" role="img" aria-label="Watercolor illustration of a garden salad and a cup of soup"></div>
    <div class="art" style="left:425px;top:36px;width:110px;height:95px;background:radial-gradient(circle,#c39055,#e9d8b8 75%,#f7f1e6)" role="img" aria-label="Watercolor illustration of a club sandwich"></div>
    <div class="art" style="left:40px;top:660px;width:90px;height:60px;background:radial-gradient(circle,#d2553f,#ecc5b5 70%,#f7eee8)" role="img" aria-label="Watercolor illustration of tomatoes and peppers"></div>

    <div class="col" style="left:40px;top:60px;width:240px">
      <h2 class="sec-title">Soup and Salad</h2>
      <p class="sub-title" style="margin:8px 0 4px">Dressings</p>
      <p class="note" style="margin-bottom:10px">Ranch, Italian, French, blue cheese, honey mustard, raspberry vinaigrette. Add chicken to any salad 2.99.</p>
      <div class="item"><h3>Soup du Jour</h3><p>Cup 2.99 · Bowl 3.99</p></div>
      <div class="item"><h3>French Onion</h3><p>Crock 4.49</p></div>
      <div class="item"><h3>Side Salad <span class="price">2.99</span></h3><p>Greens, tomato, cucumber, croutons.</p></div>
      <div class="item"><h3>Spinach Mushroom Salad <span class="price">7.99</span></h3><p>Baby spinach, mushrooms, egg, bacon, red onion.</p></div>
      <div class="item"><h3>Cranberry Feta Salad <span class="price">7.99</span></h3><p>Mixed greens, cranberries, feta, walnuts.</p></div>
      <div class="item"><h3>Chef Salad <span class="price">8.49</span></h3><p>Ham, turkey, egg, cheddar, tomato.</p></div>
      <div class="item"><h3>California Chicken Salad <span class="price">8.99</span></h3><p>Grilled chicken, avocado, bacon, tomato.</p></div>
      <div class="item"><h3>Buffalo Chicken Salad <span class="price">8.99</span></h3><p>Crispy buffalo chicken, blue cheese crumbles.</p></div>
      <div class="item"><h3>Taco Salad <span class="price">8.49</span></h3><p>Seasoned beef, salsa, sour cream, tortilla bowl.</p></div>
      <div class="item"><h3>Southwest Chicken <span class="price">8.99</span></h3><p>Black beans, corn, cheddar, chipotle ranch.</p></div>
      <div class="item"><h3>Hot Bacon Chicken Salad <span class="price">8.99</span></h3><p>Warm bacon dressing, egg, mushrooms.</p></div>
      <div class="item"><h3>Sesame Ginger Chicken Salad <span class="price">8.99</span></h3><p>Mandarin oranges, almonds, crispy noodles.</p></div>
    </div>

    <div class="col" style="left:300px;top:145px;width:235px">
      <h2 class="sec-title">Sandwiches</h2>
      <p class="note" style="margin:6px 0 10px">Served with chips and a pickle. Sub fries 1.49.</p>
      <div class="item"><h3>Triple Play Club <span class="price">8.49</span></h3><p>Turkey, ham, bacon, Swiss, on toast.</p></div>
      <div class="item"><h3>Reuben <span class="price">8.99</span></h3><p>Corned beef, kraut, Swiss, on rye.</p></div>
      <div class="item"><h3>Breaded Veal <span class="price">7.99</span></h3><p>With marinara and provolone.</p></div>
      <div class="item"><h3>Buffalo Chicken Sandwich <span class="price">8.29</span></h3><p>Hot sauce, lettuce, blue cheese.</p></div>
      <div class="item"><h3>Honey Mustard Pretzel Melt <span class="price">8.49</span></h3><p>Chicken, bacon, Swiss, pretzel bun.</p></div>
      <div class="item"><h3>Perch Sandwich <span class="price">8.99</span></h3><p>Lightly breaded, tartar sauce.</p></div>
      <div class="item"><h3>Varsity Burger <span class="price">7.99</span></h3><p>Half pound, lettuce, tomato, onion.</p></div>
      <div class="item"><h3>Flashes Burger <span class="price">8.49</span></h3><p>Bacon, cheddar, BBQ sauce.</p></div>
      <div class="item"><h3>Buckeye Burger <span class="price">8.49</span></h3><p>Mushrooms and Swiss cheese.</p></div>
      <div class="item"><h3>Firecracker Burger <span class="price">8.49</span></h3><p>Jalapeños, pepper jack, spicy mayo.</p></div>
      <div class="item"><h3>Patty Melt <span class="price">7.99</span></h3><p>Grilled onions, Swiss, on rye.</p></div>
      <div class="item"><h3>Pizza Sub <span class="price">7.49</span></h3><p>Pepperoni, sauce, mozzarella.</p></div>
      <p class="more" style="margin-top:6px">More on the next page</p>
    </div>
    <p class="more" style="position:absolute;left:150px;top:690px">Try our combo · cup of soup &amp; half salad 6.99</p>
  </section>

  <section class="page page--right">
    <div class="border-band" role="img" aria-label="Red and blue chevron border pattern"></div>
    <div class="sheet"></div>

    <div class="art" style="left:36px;top:40px;width:270px;height:150px;background:radial-gradient(ellipse at 50% 55%,#b98a4f,#e5d2b0 70%,#f6efe3)" role="img" aria-label="Watercolor illustration of a wrap with fries"></div>
    <div class="art" style="left:470px;top:36px;width:64px;height:56px;background:radial-gradient(circle,#c0604a,#ecd3c2 75%)" role="img" aria-label="Watercolor illustration of a sliced wrap"></div>
    <div class="art" style="left:360px;top:300px;width:160px;height:80px;background:linear-gradient(90deg,#d6d9e4,#e8dcc3)" role="img" aria-label="Illustration of a ballplayer beside a kids sandwich"></div>
    <div class="art" style="left:250px;top:580px;width:110px;height:80px;background:radial-gradient(circle,#e38a5a,#f1dccf 75%)" role="img" aria-label="Watercolor illustration of coffee and a soda glass"></div>

    <div class="col" style="left:320px;top:44px;width:145px">
      <h2 class="script" style="font-size:34px;line-height:1.1">Wraps</h2>
    </div>
    <div class="col" style="left:320px;top:100px;width:215px">
      <p class="note" style="margin-bottom:10px">Served in your choice of flour, wheat or tomato basil tortilla with chips.</p>
      <div class="item"><h3>Southwest Chicken <span class="price">7.99</span></h3><p>Chicken, black beans, corn, salsa.</p></div>
      <div class="item"><h3>Steak &amp; Mushroom Wrap <span class="price">8.49</span></h3><p>Shaved steak, mushrooms, Swiss.</p></div>
      <div class="item"><h3>Chicken Bacon Ranch Wrap <span class="price">7.99</span></h3><p>Grilled chicken, bacon, ranch.</p></div>
      <div class="item"><h3>Spicy Chicken Wrap <span class="price">7.99</span></h3><p>Buffalo chicken, lettuce, pepper jack.</p></div>
    </div>

    <div class="col" style="left:40px;top:205px;width:250px">
      <div class="item"><h3>Turkey Club Sub <span class="price">8.49</span></h3><p>Turkey, bacon, lettuce, tomato, mayo.</p></div>
      <div class="item"><h3>Italian Sub <span class="price">8.49</span></h3><p>Ham, salami, pepperoni, provolone, Italian dressing.</p></div>
      <div class="item"><h3>Original Philly Sub <span class="price">8.99</span></h3><p>Shaved steak or chicken, grilled onions and peppers.</p></div>
    </div>

    <div class="col" style="left:40px;top:340px;width:210px">
      <h2 class="sec-title">Beverages</h2>
      <p class="note" style="margin:6px 0 4px;letter-spacing:2px;text-transform:uppercase;font-style:normal">We proudly serve</p>
      <p class="bev-brand">Brightfizz</p>
      <p class="note" style="margin:4px 0 6px">products · 1.99 (complimentary refills)</p>
      <p class="bev-list">Cola · Diet Cola · Lemon-Lime<br>Citrus Soda · Pepper Soda<br>Root Beer · <span class="hl">Iced Tea · Lemonade</span></p>
      <div class="dots"></div>
      <p class="bev-list">Shirley Temple<br><span class="hl">Cherry Cola</span><br>Raspberry Iced Tea<br><span class="hl">2.29</span></p>
      <div class="dots"></div>
      <p class="bev-list">Coffee<br><span class="hl">1.89 (complimentary refills)</span></p>
    </div>

    <div class="col" style="left:340px;top:400px;width:195px">
      <h2 class="script" style="font-size:24px;line-height:1.15">Little Leaguers Menu</h2>
      <p class="note" style="margin:4px 0 8px">For kids 10 and under. Served with fries and a small drink. 4.99</p>
      <ul class="kids">
        <li>Grilled Cheese</li>
        <li>Mini Corn Dogs</li>
        <li>Kids Cheeseburger</li>
        <li>Kids Mac &amp; Cheese</li>
        <li>Mosaic Cheese Pizza</li>
        <li>Kids Chicken Fingers</li>
        <li>Kids Chicken Quesadilla</li>
      </ul>
    </div>
  </section>

</main>
</body>
</html>
```